Supplement Treats for Dogs and Cats Needs a Label Design

Hello everyone,We are looking for a label design for our new product. We have the container already.Attached you'll find a rough draft of the label we want, along with our logo, and the the animals we would like featured on the label. We will send along the texts, the supplement facts, QPW statement, address, and barcode once as soon as they're ready. For now, we'd like to see a more polished design.Label Measurement: 28cm x 7 cmWe might have some stock photos we want to use, I will attach it later when I have bought them. Please wait before submitting.
MIDDLE AGE

```html
<!DOCTYPE html>
<html lang="en">
<head>
<meta charset="utf-8">
<title>Kindred Paws Calming Treats Label</title>
<link rel="stylesheet" href="https://fonts.googleapis.com/css2?family=Arimo:wght@400;700&display=swap">
<style>
  :root {
    --page-bg: #f1f1f1;
    --label-green: #b3cd8b;
    --label-green-light: #bcd496;
    --brand-brown: #5a2a2a;
    --headline-grey: #4a4744;
    --body-grey: #4f4b47;
    --badge-pink: #c35f9f;
    --badge-pink-light: #d37fb5;
    --white: #ffffff;
    --photo-warm: #c98a4a;
    --photo-cool: #6c6a72;
  }
  html, body {
    margin: 0;
    padding: 0;
    width: 1200px;
    height: 1200px;
    overflow: hidden;
    background: var(--page-bg);
  }
  .canvas {
    position: relative;
    width: 1200px;
    height: 1200px;
    font-family: 'Arimo', Arial, sans-serif;
  }
  .label {
    position: absolute;
    left: 140px;
    top: 208px;
    width: 920px;
    height: 785px;
    background: radial-gradient(ellipse at 50% 40%, var(--label-green-light), var(--label-green) 70%);
    overflow: hidden;
  }
  .brand {
    position: absolute;
    left: 0;
    right: 0;
    top: 100px;
    display: flex;
    justify-content: center;
    align-items: center;
    gap: 18px;
  }
  .brand-dot {
    width: 44px;
    height: 44px;
    border-radius: 50%;
    background: var(--brand-brown);
  }
  .brand-name {
    font-weight: 700;
    font-size: 56px;
    letter-spacing: 3px;
    color: var(--brand-brown);
    line-height: 1;
  }
  .product-title {
    position: absolute;
    left: 104px;
    top: 262px;
    width: 378px;
    text-align: right;
  }
  .product-title h1 {
    margin: 0;
    font-weight: 700;
    font-size: 76px;
    line-height: 1;
    letter-spacing: 1px;
    color: var(--headline-grey);
  }
  .product-title p {
    margin: 2px 0 0;
    font-size: 33px;
    line-height: 1.1;
    color: var(--body-grey);
  }
  .divider {
    position: absolute;
    left: 502px;
    top: 262px;
    width: 3px;
    height: 116px;
    background: var(--headline-grey);
  }
  .taste-claim {
    position: absolute;
    left: 520px;
    top: 268px;
    margin: 0;
    font-size: 30px;
    line-height: 37px;
    color: var(--body-grey);
  }
  .pet-photo {
    position: absolute;
    left: 90px;
    top: 385px;
    width: 660px;
    height: 372px;
    border-radius: 24px;
    background: linear-gradient(100deg, var(--photo-warm) 0%, #b9854f 45%, var(--photo-cool) 65%, #5c5a62 100%);
    opacity: 0.85;
  }
  .count-badge {
    position: absolute;
    left: 297px;
    top: 693px;
    width: 333px;
    height: 68px;
    border-radius: 6px 6px 0 0;
    background: linear-gradient(180deg, var(--badge-pink-light), var(--badge-pink));
    color: var(--white);
    text-align: center;
    font-size: 25px;
    line-height: 30px;
    padding-top: 4px;
    box-sizing: border-box;
  }
  .count-badge strong {
    font-weight: 700;
  }
</style>
</head>
<body>
<div class="canvas">
  <section class="label">
    <div class="brand">
      <span class="brand-dot"></span>
      <span class="brand-name">KINDRED PAWS</span>
    </div>

    <div class="product-title">
      <h1>CALMING</h1>
      <p>For dogs and cats</p>
    </div>

    <div class="divider"></div>

    <p class="taste-claim">MADE WITH<br>THAT TASTE<br>PETS LOVE.</p>

    <div class="pet-photo" role="img" aria-label="Photo of a golden retriever lying down with a grey and white cat nuzzling against it"></div>

    <div class="count-badge"><strong>60</strong> SOFT<br>CHEWABLE TREATS</div>
  </section>
</div>
</body>
</html>
```